Marrow Airways Group Envelope, Letterhead, Business Card Design

I need designs for a new company letterhead, business cards, and envelopes. These designs will need to be presented using 5 different company logos for the different divisions that are managed under the Marrow Airways Group umbrella (company names listed below). The member of QTFL logo should also be included.
- Marrow Airways Group
- Marrow Jet Management
- Marrow Jet Charter
- Marrow Pilot Services
- Marrow Aircraft Sales
- Marrow Flight Training

Logos for the various companies are attached as well as a screen shot of the main page of our website.

```html
<!DOCTYPE html>
<html lang="en">
<head>
<meta charset="utf-8">
<title>Marrow Airways Group – Business Card</title>
<link rel="stylesheet" href="https://fonts.googleapis.com/css2?family=Montserrat:wght@400;500;600;700&display=swap">
<style>
  :root {
    --bg-light: #d2d1cd;
    --bg-dark: #9f9e9a;
    --paper: #ffffff;
    --brand-blue: #0b62b5;
    --brand-blue-deep: #0a549d;
    --ink: #1d1d1f;
    --ink-soft: #3a3a3c;
    --mist: #e6e6e6;
  }
  * { margin: 0; padding: 0; box-sizing: border-box; }
  html, body { width: 1200px; height: 857px; overflow: hidden; }
  body {
    background: linear-gradient(120deg, var(--bg-dark) 0%, var(--bg-light) 100%);
    font-family: "Montserrat", sans-serif;
    position: relative;
  }
  .card {
    position: absolute;
    top: 150px;
    width: 320px;
    height: 557px;
    border-radius: 3px;
    box-shadow: 0 18px 40px rgba(0,0,0,0.25);
    overflow: hidden;
  }
  .card--front { left: 220px; background: var(--paper); border-bottom: 4px solid var(--brand-blue); }
  .card--back { left: 660px; background: var(--brand-blue); }

  .front-logo {
    position: absolute; top: 64px; right: 34px;
    text-align: right;
    display: flex; align-items: center; gap: 10px;
  }
  .front-logo__mark { width: 14px; height: 14px; border-radius: 50%; background: var(--brand-blue); }
  .front-logo__name {
    font-weight: 700; font-size: 19px; letter-spacing: 1.5px;
    color: var(--brand-blue); text-transform: uppercase; line-height: 1.15;
  }
  .front-decoration {
    position: absolute; top: 230px; left: 0; width: 320px; height: 90px;
    background: linear-gradient(90deg, rgba(230,230,230,0) 0%, var(--mist) 50%, rgba(230,230,230,0) 100%);
  }
  .contact { position: absolute; left: 34px; bottom: 54px; }
  .contact__name { font-weight: 700; font-size: 20px; color: var(--brand-blue); }
  .contact__title { font-weight: 600; font-size: 13px; color: var(--ink); margin-top: 4px; }
  .contact__rule { width: 40px; height: 2px; background: var(--brand-blue); margin: 14px 0 16px; }
  .contact__list { list-style: none; }
  .contact__item {
    display: flex; align-items: center; gap: 10px;
    font-size: 12.5px; color: var(--ink-soft); margin-bottom: 8px;
  }
  .contact__icon { width: 12px; height: 12px; flex: none; }

  .divisions {
    position: absolute; inset: 46px 30px 40px;
    display: flex; flex-direction: column; justify-content: space-between;
    align-items: center; text-align: center;
  }
  .division__name {
    font-weight: 600; font-size: 20px; letter-spacing: 2px;
    color: var(--brand-blue-deep); text-transform: uppercase; line-height: 1.2;
  }
  .membership { display: flex; flex-direction: column; align-items: center; }
  .membership__label { font-size: 10px; color: var(--brand-blue-deep); font-weight: 600; }
  .membership__name { font-size: 30px; font-weight: 600; letter-spacing: 3px; color: var(--brand-blue-deep); }
</style>
</head>
<body>
  <section class="card card--front">
    <div class="front-logo">
      <span class="front-logo__mark"></span>
      <span class="front-logo__name">Marrow<br>Airways Group</span>
    </div>
    <div class="front-decoration" role="img" aria-label="Faint brand decoration area"></div>
    <div class="contact">
      <p class="contact__name">Daniel Hartley</p>
      <p class="contact__title">Development Executive Officer</p>
      <div class="contact__rule"></div>
      <ul class="contact__list">
        <li class="contact__item">
          <svg class="contact__icon" viewBox="0 0 12 12"><path d="M3 1l2 2.5-1 1.2c.6 1.3 1.6 2.3 2.9 2.9L8 6.6 10.5 8.6 9.6 10.6C5.5 10.4 1.6 6.5 1.4 2.4z" fill="var(--brand-blue)"/></svg>
          +874 5550 0192
        </li>
        <li class="contact__item">
          <svg class="contact__icon" viewBox="0 0 12 12"><rect x="1" y="2.5" width="10" height="7" fill="var(--brand-blue)"/><path d="M1 2.5l5 4 5-4" stroke="#fff" stroke-width="1" fill="none"/></svg>
          daniel@marrowairwaysgroup.com
        </li>
        <li class="contact__item">
          <svg class="contact__icon" viewBox="0 0 12 12"><circle cx="6" cy="6" r="5" fill="none" stroke="var(--brand-blue)" stroke-width="1.2"/><path d="M1 6h10M6 1c-2.5 3-2.5 7 0 10M6 1c2.5 3 2.5 7 0 10" fill="none" stroke="var(--brand-blue)" stroke-width="0.8"/></svg>
          marrowairwaysgroup.com
        </li>
      </ul>
    </div>
  </section>

  <section class="card card--back">
    <div class="divisions">
      <p class="division__name">Marrow<br>Jet Charter</p>
      <p class="division__name">Marrow<br>Jet Management</p>
      <p class="division__name">Marrow<br>Pilot Services</p>
      <p class="division__name">Marrow<br>Aircraft Sales</p>
      <p class="division__name">Marrow<br>Flight Training</p>
      <div class="membership">
        <span class="membership__label">member of</span>
        <span class="membership__name">QTFL</span>
      </div>
    </div>
  </section>
</body>
</html>
```